Postcard Design hearing aid sales & service. Free hearing test . Fresh batteries

Cedar Hollow Hearing Aid Device Center . Located at 417 Marlowe Ln Abilene Texas 79605 Ph 325-555-0148.
Hours Mon thru Thurs 9:00am - 5:00pm closed for lunch 12:00pm - 1:00pm . Fri open 9:00am - 1:00pm
Hearing Test n/c Hearing aid adjustment & cleaning of hearing aids n/c . Fresh batteries buy one 1/2 off on 2nd pack. Limited time. Walk-in welcome Appointments appreciated. THIS MONTH ONLY Special discounts on new state of the art hearing aids w/remote. .

```html
<!DOCTYPE html>
<html lang="en">
<head>
<meta charset="utf-8">
<title>Cedar Hollow Hearing Aid Device Center – Postcard</title>
<link rel="stylesheet" href="https://fonts.googleapis.com/css2?family=Marcellus&family=Open+Sans:ital,wght@0,400;0,600;0,700;1,400&family=Bebas+Neue&display=swap">
<style>
  :root {
    --teal: #2e9db0;
    --teal-light: #93d3d7;
    --tan: #ab9886;
    --box: #d7eef0;
    --brown: #6e5b3f;
    --label: #9a7f5f;
    --ink: #111;
    --muted: #555;
    --white: #fff;
  }
  * { box-sizing: border-box; margin: 0; padding: 0; }
  html, body { width: 1200px; height: 902px; overflow: hidden; background: #fff; }
  .postcard {
    position: relative; width: 1200px; height: 902px; overflow: hidden;
    background: linear-gradient(180deg, #fff 60%, #f3f4f4 100%);
    font-family: "Open Sans", Arial, sans-serif; color: var(--ink);
  }
  .shapes { position: absolute; inset: 0; }
  .hours {
    position: absolute; left: 49px; top: 34px; color: var(--white);
    font-size: 19px; line-height: 1.2; white-space: nowrap;
  }
  .hours .title { font-size: 20px; margin-bottom: 6px; }
  .hours .note { font-size: 12px; }
  .business-name {
    position: absolute; left: 400px; right: 40px; top: 28px;
    font-family: "Marcellus", Georgia, serif; font-weight: 400;
    color: var(--white); font-size: 72px; line-height: 76px; text-align: center;
    white-space: nowrap;
  }
  .services { position: absolute; left: 560px; right: 0; top: 0; text-align: center; white-space: nowrap; }
  .services h2 { position: absolute; left: 0; right: 0; top: 236px; font-weight: 400; font-size: 39px; line-height: 1.2; }
  .services p { position: absolute; left: 0; right: 0; top: 310px; font-size: 21px; }
  .offer {
    position: absolute; top: 451px; width: 226px; height: 206px;
    background: var(--box); border-radius: 12px;
    box-shadow: 2px 4px 8px rgba(0,0,0,.18); text-align: center;
  }
  .offer.batteries { left: 691px; }
  .offer.discounts { left: 933px; }
  .offer .label { margin-top: 14px; font-size: 17px; font-weight: 600; color: var(--label); }
  .offer .headline {
    font-family: "Bebas Neue", Impact, sans-serif; color: var(--brown);
    font-size: 33px; line-height: 38px; margin-top: 28px;
  }
  .offer.discounts .headline { margin-top: 34px; }
  .offer .detail { font-size: 14px; font-weight: 600; color: var(--brown); line-height: 22px; }
  .offer .fine { position: absolute; bottom: 10px; left: 0; right: 0; font-size: 15px; font-weight: 600; color: var(--label); }
  .visit { position: absolute; left: 660px; right: 40px; top: 0; text-align: center; white-space: nowrap; }
  .visit .welcome { position: absolute; left: 0; right: 0; top: 696px; font-style: italic; color: var(--muted); font-size: 19px; }
  .visit .address { position: absolute; left: 0; right: 0; top: 736px; font-size: 21px; }
  .phone {
    position: absolute; left: 790px; top: 812px; color: var(--white);
    font-size: 44px; font-weight: 700; display: flex; align-items: center; gap: 22px;
    white-space: nowrap;
  }
  .phone svg { width: 34px; height: 34px; }
</style>
</head>
<body>
<div class="postcard">
  <svg class="shapes" width="1200" height="902" viewBox="0 0 1200 902">
    <polygon class="hours-panel" points="0,0 290,0 398,212 0,212" fill="var(--tan)"/>
    <polygon class="header-band" points="304,0 1200,0 1200,204 412,204" fill="var(--teal)"/>
    <rect class="header-rule" x="412" y="204" width="788" height="8" fill="var(--tan)"/>
    <rect class="footer-rule" x="0" y="778" width="1200" height="6" fill="var(--teal-light)"/>
    <rect class="footer-band" x="0" y="784" width="1200" height="118" fill="var(--tan)"/>
    <circle class="photo-ring" cx="235" cy="580" r="412" fill="var(--teal-light)"/>
    <circle class="photo-gap" cx="235" cy="580" r="404" fill="var(--white)"/>
    <defs>
      <radialGradient id="photoTone" cx="40%" cy="40%" r="70%">
        <stop offset="0" stop-color="#e9dcd2"/>
        <stop offset=".6" stop-color="#cfc6c0"/>
        <stop offset="1" stop-color="#a7a9ad"/>
      </radialGradient>
    </defs>
    <circle class="photo" cx="235" cy="580" r="394" fill="url(#photoTone)" role="img" aria-label="Photo of a smiling senior couple embracing"/>
  </svg>

  <div class="hours">
    <div class="title">HOURS</div>
    <div>Mon - Thru -Thurs</div>
    <div>9:00am - 5:00pm</div>
    <div class="note">(closed for lunch 12:00pm - 1:00pm.)</div>
    <div>Fri open 9:00am - 1:00pm</div>
  </div>

  <h1 class="business-name">Cedar Hollow Hearing<br>Aid Device Center</h1>

  <div class="services">
    <h2>Hearing Aid Sales &amp; Service</h2>
    <p>FREE HEARING TEST. FRESH BATTERIES</p>
  </div>

  <div class="offer batteries">
    <div class="label">FRESH BATTERIES</div>
    <div class="headline">Buy one 50% off<br>on 2nd pack</div>
    <div class="fine">LIMITED TIME</div>
  </div>
  <div class="offer discounts">
    <div class="label">THIS MONTH ONLY</div>
    <div class="headline">Special discounts</div>
    <div class="detail">on new state of the art<br>hearing aids w/remote</div>
  </div>

  <div class="visit">
    <p class="welcome">Walk-in welcome Appointments appreciated!</p>
    <p class="address">417 Marlowe Ln Abilene Texas 79605</p>
  </div>

  <div class="phone">
    <svg viewBox="0 0 24 24" aria-hidden="true"><path fill="#fff" d="M6.6 10.8a15.1 15.1 0 0 0 6.6 6.6l2.2-2.2a1 1 0 0 1 1-.25 11.4 11.4 0 0 0 3.6.57 1 1 0 0 1 1 1V20a1 1 0 0 1-1 1A17 17 0 0 1 3 4a1 1 0 0 1 1-1h3.5a1 1 0 0 1 1 1c0 1.25.2 2.45.57 3.570a1 1 0 0 1-.25 1z"/></svg>
    <span>325-555-0148</span>
  </div>
</div>
</body>
</html>
```